Financial Service Company Need Business Card Design

This is a new startup company, first of its kind to offer this service. We facilitate the movement of deposit funds electronically between home buyers and real estate brokerages.Our customers are DOMIVANS®, real estate brokerages, and home buyers, we identify ourselves as a financial/technology company.
Not looking for anything too flashy. Just a clean design that shows the logo, contact info, etc. Company colors can be seen on attached logo, and 'coming soon page'
www.quorvanta.ca

```html
<!DOCTYPE html>
<html lang="en">
<head>
<meta charset="utf-8">
<title>Quorvanta Business Card</title>
<link rel="stylesheet" href="https://fonts.googleapis.com/css2?family=Open+Sans:wght@400;600;700&family=Ubuntu:wght@500&display=swap">
<style>
  :root {
    --backdrop: #dcd8d1;
    --card-white: #f4f4f4;
    --card-black: #111214;
    --card-black-soft: #2a2b2e;
    --brand-orange: #e8622a;
    --logo-grey: #6e6e70;
    --ink: #1b1b1b;
    --light-text: #e9e9e9;
  }
  * { box-sizing: border-box; margin: 0; padding: 0; }
  html, body {
    width: 1200px; height: 1023px; overflow: hidden;
    background: var(--backdrop);
    font-family: "Open Sans", Arial, sans-serif;
  }
  .sheet {
    position: relative; width: 1200px; height: 1023px;
    display: flex; flex-direction: column; align-items: center; justify-content: center; gap: 60px;
  }
  .card {
    position: relative; width: 700px; height: 400px; overflow: hidden;
    box-shadow: 0 10px 30px rgba(0,0,0,0.25);
  }
  /* Front */
  .card-front { background: linear-gradient(160deg, var(--card-black-soft), var(--card-black) 60%); }
  .front-identity {
    position: absolute; left: 0; top: 0; width: 100%; height: 215px;
    background: var(--card-white); padding: 38px 0 0 44px;
  }
  .brand { display: flex; align-items: center; gap: 18px; }
  .brand-square { width: 46px; height: 46px; background: var(--brand-orange); }
  .brand-name {
    font-family: "Ubuntu", "Open Sans", sans-serif; font-weight: 500;
    font-size: 66px; line-height: 1; color: var(--logo-grey); letter-spacing: -1px;
  }
  .person-name {
    margin-top: 26px; color: var(--brand-orange); font-weight: 700; font-size: 22px; letter-spacing: 0.5px;
  }
  .person-title { color: var(--ink); font-size: 14px; letter-spacing: 1px; margin-top: 2px; }
  .contact-list {
    position: absolute; left: 44px; top: 240px; list-style: none;
    color: var(--light-text); font-size: 16px;
  }
  .contact-list li { display: flex; align-items: center; gap: 12px; margin-bottom: 9px; }
  .contact-icon { width: 18px; height: 18px; background: var(--brand-orange); border-radius: 2px; display: flex; align-items: center; justify-content: center; }
  .address {
    position: absolute; left: 44px; top: 350px;
    color: var(--brand-orange); font-weight: 700; font-size: 16px; letter-spacing: 0.3px;
  }
  .corner-stripes { position: absolute; right: 0; top: 0; }
  /* Back */
  .card-back { background: linear-gradient(160deg, #2c2d30, var(--card-black) 55%); }
  .back-stripes { position: absolute; inset: 0; }
  .back-brand {
    position: absolute; inset: 0; display: flex; align-items: center; justify-content: center; gap: 18px;
  }
  .back-brand .brand-square { background: #f2f2f2; }
  .back-brand .brand-name { color: #f2f2f2; }
</style>
</head>
<body>
<main class="sheet">
  <section class="card card-front">
    <svg class="corner-stripes" width="200" height="215" viewBox="0 0 200 215" aria-hidden="true">
      <polygon points="60,0 100,0 200,130 200,182" fill="var(--brand-orange)"/>
      <polygon points="118,0 150,0 200,66 200,108" fill="var(--brand-orange)"/>
      <polygon points="168,0 200,0 200,42" fill="var(--brand-orange)"/>
    </svg>
    <div class="front-identity">
      <div class="brand">
        <span class="brand-square"></span>
        <span class="brand-name">Quorvanta</span>
      </div>
      <p class="person-name">DANIEL MARSH</p>
      <p class="person-title">PRESIDENT</p>
    </div>
    <svg class="corner-stripes" width="200" height="215" viewBox="0 0 200 215" aria-hidden="true">
      <polygon points="0,0 60,0 200,182 200,215 150,215" fill="#141517"/>
      <polygon points="60,0 100,0 200,130 200,182" fill="var(--brand-orange)"/>
      <polygon points="118,0 150,0 200,66 200,108" fill="var(--brand-orange)"/>
      <polygon points="168,0 200,0 200,42" fill="var(--brand-orange)"/>
    </svg>
    <ul class="contact-list">
      <li>
        <span class="contact-icon"><svg width="12" height="12" viewBox="0 0 12 12"><path d="M2 1h3l1 3-2 1a7 7 0 0 0 3 3l1-2 3 1v3c-5 0-9-4-9-9z" fill="#fff"/></svg></span>
        555-010-4821
      </li>
      <li>
        <span class="contact-icon"><svg width="12" height="12" viewBox="0 0 12 12"><rect x="1" y="3" width="10" height="7" fill="#fff"/><path d="M1 3l5 4 5-4" stroke="var(--brand-orange)" fill="none"/></svg></span>
        daniel@quorvanta.ca
      </li>
      <li>
        <span class="contact-icon"><svg width="12" height="12" viewBox="0 0 12 12"><circle cx="6" cy="6" r="4.5" stroke="#fff" fill="none"/><path d="M1.5 6h9M6 1.5v9" stroke="#fff"/></svg></span>
        www.quorvanta.ca
      </li>
    </ul>
    <p class="address">1100 LARKFIELD STREET, ANYWHERE, ANY CITY</p>
  </section>

  <section class="card card-back">
    <svg class="back-stripes" width="700" height="400" viewBox="0 0 700 400" aria-hidden="true">
      <polygon points="0,250 700,90 700,150 0,310" fill="rgba(255,255,255,0.04)"/>
      <polygon points="0,330 700,170 700,210 0,370" fill="rgba(255,255,255,0.03)"/>
    </svg>
    <div class="back-brand">
      <span class="brand-square"></span>
      <span class="brand-name">Quorvanta</span>
    </div>
  </section>
</main>
</body>
</html>
```